Volmira Logo and business card

We need a business card and logo, we are currently using a logo that we like but would like to be a bit more streamlined. We deal with very high end clients and our business card needs to reflect that. We would love to see and hire somebody that can deliver a very MODERN, simple design. With he main front of the card to be black with either a red lettering or White to provide great contrast. I would like to have a minimalist abstract picture of a heavy machine on it but it is not a requirement ( most likely an Crane ( a bold heron crane with a bucket would be perfect or maybe a vendari 270 XT )) If it keeps in line with being a classic simple, and modern design. Letterpress is also an option where it gives it a great look and texture, the card will be printed on a thick stock. On the back there needs to be a star included somewhere on the card and design, this represents the first generation that started the company back in 1936 therefore it is a sentimental addition ( make it modern and simple)
We do not want a cheesy construction template. We do heavy site work, aka we use excavators, payloaders, off road rok j40 trucks, very big fun toys.
There is a huge chance to get the web design as well for the winning design.
Have fun, cannot wait to see the designs!
In addition, we'd like to point out that our primary need and priority is still the BUSINESS CARD design itself. The logo has to complement the overall look of the business card, but it is secondary to the card's look. Please keep this in mind.
Thank you,
Gerald
Target Market(s)
General Contractors, upscale home owners ( house values of 1M plus)
and commercial property owners.
Projects range from $5000 to 1 million.
Industry/Entity Type
Construction
Requirements
Must have
- Star incorporated into design
Nice to have
- an abstract heavy site work machine ( pics attached) If it keeps in line with being a classic simple, and modern design.
I would like to have black and red on the design since all the lettering on the trucks is red, but i will let the designer take care of that.

```html
<!DOCTYPE html>
<html lang="en">
<head>
<meta charset="utf-8">
<title>Volmira Industries – Business Card</title>
<link rel="stylesheet" href="https://fonts.googleapis.com/css2?family=Source+Sans+3:wght@300;400;800&display=swap">
<style>
  :root {
    --canvas: #ffffff;
    --frame-dash: #d4d4d4;
    --card-black: #151515;
    --logo-ink: #f4f4f4;
    --accent: #c4511f;
    --card-white: #ffffff;
    --text: #1c1c1c;
    --machine-light: #ececec;
    --machine-mid: #d6d6d6;
  }
  * { margin: 0; padding: 0; box-sizing: border-box; }
  html, body { width: 1132px; height: 1200px; overflow: hidden; background: var(--canvas); }
  body { font-family: "Source Sans 3", "Myriad Pro", Arial, sans-serif; color: var(--text); position: relative; }

  .presentation-frame {
    position: absolute; inset: 2px;
    border: 2px dashed var(--frame-dash);
  }

  .card {
    position: absolute; left: 208px; width: 705px; height: 373px;
    box-shadow: 0 14px 18px -6px rgba(0,0,0,0.45);
    overflow: hidden;
  }
  .card--front { top: 151px; background: var(--card-black); }
  .card--back { top: 647px; background: var(--card-white); }

  .wordmark {
    position: absolute; left: 133px; top: 112px;
    font-weight: 800; color: var(--logo-ink);
    font-size: 116px; line-height: 1; letter-spacing: -3px;
    white-space: nowrap;
  }
  .wordmark__rule {
    position: absolute; left: 133px; right: 0; top: 223px;
    height: 3px; background: var(--accent);
  }
  .wordmark__sub {
    position: absolute; left: 133px; top: 234px;
    font-weight: 300; color: var(--logo-ink);
    font-size: 34px; letter-spacing: 26px; line-height: 1;
    white-space: nowrap;
  }

  .machine-illustration {
    position: absolute; right: 0; top: 4px; width: 280px; height: 221px;
  }

  .contact__name {
    position: absolute; left: 26px; top: 178px;
    font-size: 41px; font-weight: 400; line-height: 1;
  }
  .contact__rule {
    position: absolute; left: 0; width: 568px; top: 232px;
    height: 2px; background: var(--accent);
  }
  .heritage-star {
    position: absolute; left: 576px; top: 223px; width: 20px; height: 20px;
  }
  .contact__details {
    position: absolute; left: 26px; top: 235px;
    list-style: none; font-size: 23px; line-height: 30.5px; font-weight: 400;
  }
  .contact__sep { display: inline-block; margin: 0 14px; }
</style>
</head>
<body>
  <div class="presentation-frame"></div>

  <section class="card card--front" aria-label="Card front">
    <div class="wordmark">VOLMIRA</div>
    <div class="wordmark__rule"></div>
    <div class="wordmark__sub">INDUSTRIES</div>
  </section>

  <section class="card card--back" aria-label="Card back">
    <svg class="machine-illustration" role="img" aria-label="Light line sketch of an excavator with boom and bucket" viewBox="0 0 280 221">
      <defs>
        <linearGradient id="machineTone" x1="0" y1="0" x2="1" y2="1">
          <stop offset="0" stop-color="var(--machine-light)"/>
          <stop offset="1" stop-color="var(--machine-mid)"/>
        </linearGradient>
      </defs>
      <rect width="280" height="221" fill="url(#machineTone)" opacity="0.55"/>
    </svg>

    <h1 class="contact__name">Dario Volmira</h1>
    <div class="contact__rule"></div>
    <svg class="heritage-star" viewBox="0 0 20 20" aria-label="Heritage star">
      <polygon points="10,1 12.6,7.4 19.5,7.6 14.1,11.9 16,18.5 10,14.7 4,18.5 5.9,11.9 0.5,7.6 7.4,7.4" fill="var(--accent)"/>
    </svg>
    <ul class="contact__details">
      <li>CEO</li>
      <li>dario@volmiraindustries.com</li>
      <li>+1 (555) 014-2290</li>
      <li>14 Larkin Way<span class="contact__sep">•</span>Harbor Point, NY 11990</li>
    </ul>
  </section>
</body>
</html>
```